Off Campus Housing website service for universities needs corporate brochure

We need a corporate brochure targeted at universities to get them to partner with us to offer an Off-Campus Housing website with housing listings and educational resources for their students. We provide hosted software and support, off-campus housing listings, and educational resources to embed in the university website (i.e http://rentalhub.brx.edu); the university promotes the service to off-campus students, parents, and faculty/staff. We have a dedicated account executive to work with each university to promote the website to property managers in the schools area who pay to list their properties on the site. We currently partner with over 100 colleges and universities across the country to serve the needs of their off-campus students. Our corporate website is: www.lodgebridgealliance.com.
Updates

Target Market(s)

Universities and Colleges

Industry/Entity Type

Marketing

Font styles to use
Serif

Requirements
Must have
• Our logo
• Our website (www.lodgebridgealliance.com)
• Contact information (this is different than what we used on our previous brochure, image attached):
• Email: sales@lodgebridgealliance.com
• Student image(s) - must be diverse
• Phone: 866-402-7719
Nice to have
• University/Campus image (generic)

```html
<!DOCTYPE html>
<html lang="en">
<head>
<meta charset="utf-8">
<title>Off Campus Housing – Lodgebridge Alliance brochure</title>
<link rel="stylesheet" href="https://fonts.googleapis.com/css2?family=Cinzel:wght@700&family=EB+Garamond:ital,wght@0,400;0,500;1,600&display=swap">
<style>
  :root {
    --backdrop: #222222;
    --paper: #ffffff;
    --royal: #0f4fa3;
    --royal-deep: #0a3f8c;
    --gold: #d9a21c;
    --ink: #1d1d1d;
    --text-blue: #1f4f9c;
    --shadow: rgba(20, 20, 10, 0.65);
  }
  * { margin: 0; padding: 0; box-sizing: border-box; }
  html, body { width: 1200px; height: 1200px; overflow: hidden; background: var(--backdrop); }
  .brochure {
    position: absolute; left: 60px; top: 182px; width: 1080px; height: 835px;
    overflow: hidden; background: var(--paper);
    font-family: "EB Garamond", Georgia, serif;
  }
  .brochure svg.artwork { position: absolute; inset: 0; }
  .headline {
    position: absolute; left: 46px; top: 44px; white-space: nowrap;
    font-family: "Cinzel", Georgia, serif; font-weight: 700;
    font-size: 40px; color: var(--gold); letter-spacing: 0.3px; line-height: 1;
  }
  .tagline {
    position: absolute; left: 126px; top: 88px; white-space: nowrap;
    font-size: 27px; font-weight: 400; color: var(--ink); line-height: 1;
  }
  .brand {
    position: absolute; left: 866px; top: 60px; white-space: nowrap;
    display: flex; align-items: center; gap: 8px;
    font-weight: 500; font-size: 20px; color: var(--paper); letter-spacing: 0.5px; line-height: 1;
  }
  .brand-square { width: 11px; height: 11px; background: var(--paper); }
  .testimonial {
    position: absolute; left: 760px; top: 416px; width: 280px; white-space: nowrap;
    text-align: center; font-style: italic; font-weight: 600;
    font-size: 15px; line-height: 19px; color: var(--paper);
    text-shadow: 0 0 2px var(--royal-deep), 0 0 2px var(--royal-deep), 0 0 1px var(--royal-deep);
  }
  .feature { position: absolute; text-align: center; color: var(--paper); white-space: nowrap; }
  .feature h2 { font-weight: 400; font-size: 30px; color: var(--gold); line-height: 1; margin-bottom: 8px; }
  .feature p { font-size: 15px; font-weight: 400; line-height: 19px; }
  .feature-students { left: 16px; top: 626px; width: 330px; }
  .feature-university { left: 752px; top: 624px; width: 312px; }
  .partner-card {
    position: absolute; left: 352px; top: 570px; width: 376px; text-align: center; white-space: nowrap;
  }
  .partner-card h2 { font-weight: 400; font-size: 30px; color: var(--gold); line-height: 37px; margin-bottom: 4px; }
  .partner-card p { font-size: 15px; font-weight: 400; color: var(--text-blue); line-height: 19.2px; }
  .contact {
    position: absolute; left: 0; top: 794px; width: 1080px; text-align: center; white-space: nowrap;
    font-size: 17px; font-weight: 500; color: var(--paper); letter-spacing: 0.3px;
    text-shadow: 0 1px 3px var(--shadow);
  }
  .contact span + span::before { content: "\2022"; margin: 0 14px; color: var(--gold); }
</style>
</head>
<body>
<main class="brochure">
  <svg class="artwork" width="1080" height="835" viewBox="0 0 1080 835">
    <defs>
      <linearGradient id="studentTone" x1="0" y1="0" x2="1" y2="1">
        <stop offset="0" stop-color="#d9a24a"/>
        <stop offset="0.5" stop-color="#c9b8a4"/>
        <stop offset="1" stop-color="#6e3f2a"/>
      </linearGradient>
      <linearGradient id="buildingTone" x1="0" y1="0" x2="0" y2="1">
        <stop offset="0" stop-color="#4f7fc4"/>
        <stop offset="0.3" stop-color="#e8ecf0"/>
        <stop offset="0.75" stop-color="#d8d6d2"/>
        <stop offset="1" stop-color="#6a2e24"/>
      </linearGradient>
      <linearGradient id="lawnTone" x1="0" y1="0" x2="1" y2="0">
        <stop offset="0" stop-color="#a4662e"/>
        <stop offset="0.45" stop-color="#8e9a2c"/>
        <stop offset="1" stop-color="#b07a34"/>
      </linearGradient>
    </defs>

    <rect class="photo-student" x="0" y="140" width="520" height="500" fill="url(#studentTone)"
          role="img" aria-label="Photo: smiling student with a laptop at an outdoor table under autumn trees"/>
    <rect class="photo-campus" x="500" y="0" width="580" height="640" fill="url(#buildingTone)"
          role="img" aria-label="Photo: white-columned campus building with balcony railings under blue sky"/>
    <rect class="photo-lawn" x="0" y="722" width="1080" height="113" fill="url(#lawnTone)"
          role="img" aria-label="Photo: autumn campus lawn with long shadows"/>

    <polygon class="header-band" points="0,158 144,194 1080,0 1080,16 144,212 0,176" fill="var(--royal)"/>
    <polygon class="header-field" points="0,0 1080,0 144,194 0,158" fill="var(--paper)"/>

    <rect class="feature-bar" x="0" y="622" width="1080" height="102" fill="var(--royal)"/>

    <path class="partner-card-shape"
          d="M340 568 Q420 548 520 556 Q640 550 700 552 Q742 560 748 600 L752 735 Q748 768 700 762 Q600 770 520 766 Q420 774 370 768 Q340 766 338 735 L336 680 Q328 660 338 640 Z"
          fill="var(--paper)"/>
  </svg>

  <h1 class="headline">OFF CAMPUS HOUSING</h1>
  <p class="tagline">at your students’ fingertips</p>

  <div class="brand"><span class="brand-square"></span>Lodgebridge Alliance</div>

  <blockquote class="testimonial">
    “Very helpful website all around! It<br>
    definitely helped ease the process of<br>
    looking for an apartment.”<br>
    -Dana, Harlow State Student
  </blockquote>

  <section class="feature feature-students">
    <h2>For your students</h2>
    <p>A single site to find off-campus housing,<br>sublets, roommates, furniture, and education<br>about off-campus living.</p>
  </section>

  <section class="partner-card">
    <h2>Partner with the<br>industry leader</h2>
    <p>We work with over 100 university partners,<br>1.4 million off-campus students, and offer<br>a variety of funding models to suit your<br>university’s unique needs. Funding models<br>may include potential revenue sharing.</p>
  </section>

  <section class="feature feature-university">
    <h2>For your university.</h2>
    <p>A custom off-campus housing program<br>designed to meet the specific needs of your<br>institution’s off-campus environment</p>
  </section>

  <p class="contact">
    <span>www.lodgebridgealliance.com</span><span>sales@lodgebridgealliance.com</span><span>866-402-7719</span>
  </p>
</main>
</body>
</html>
```